Kestrel Electrics - Electrician company flyers for new clients

I want a flyer that will be dropped into mailboxes and will hopefully stand out more that the ones i have tried to mock up. I have attached my latest design to give you an idea but it is rather boring.

The aim is obviously to entice new customers into calling me for any electrical work, mainly domestic but i also do commercial work.
I will also upload a photo of my business card so that it can be used as a reference and my website is www.kestrelelectrics-example.co.nz for any extra information.

Ideally the flyer will be DL size
measurements from printmondo is that's any help
Document Trim Size
99 x 210 mm
1169 x 2480 pixels
Full Bleed Size
102 x 213 mm
1205 x 2516 pixels

Target Market(s)

Domestic electrical works

Industry/Entity Type

Electrician

Requirements
Must have
• all of my contact details -
• Dean Harwood
• Dean@kestrelelectrics-example.co.nz
• 027 5832 094
• www.kestrelelectrics-example.co.nz
• A little write up similar to the one written on my draft but there's probably alot of room for improvement as my writing skills are lacking.
Nice to have
• clear and concise writing so that people wont throw it away before reading

```html
<!DOCTYPE html>
<html lang="en">
<head>
<meta charset="utf-8">
<title>Kestrel Electrics – Flyer</title>
<link href="https://fonts.googleapis.com/css2?family=Montserrat:wght@400;600;700;800&display=swap" rel="stylesheet">
<style>
  :root {
    --brand-blue: #00a4e4;
    --brand-grey: #818181;
    --paper: #ffffff;
    --ink-light: #ffffff;
  }
  * { margin: 0; padding: 0; box-sizing: border-box; }
  html, body { width: 1200px; height: 2506px; overflow: hidden; background: var(--paper); }
  .flyer {
    position: relative;
    width: 1200px;
    height: 2506px;
    overflow: hidden;
    background: var(--paper);
    font-family: "Montserrat", sans-serif;
    color: var(--ink-light);
  }
  .brand-name {
    position: absolute;
    top: 110px;
    left: 92px;
    width: 1020px;
    height: 345px;
    display: flex;
    align-items: center;
    gap: 40px;
    color: var(--brand-blue);
    font-weight: 800;
    text-transform: uppercase;
  }
  .brand-name__mark {
    width: 160px;
    height: 160px;
    background: var(--brand-blue);
    flex: none;
  }
  .brand-name__text {
    font-size: 124px;
    line-height: 1.05;
    letter-spacing: 4px;
  }
  .roof-art {
    position: absolute;
    top: 0;
    left: 0;
  }
  .roof-art .house { fill: var(--brand-blue); }
  .roof-art .eave { fill: var(--brand-grey); }
  .headline {
    position: absolute;
    top: 870px;
    left: 0;
    width: 1190px;
    text-align: center;
    font-weight: 600;
    font-size: 66px;
    line-height: 84px;
  }
  .body-copy {
    position: absolute;
    top: 1198px;
    left: 177px;
    width: 853px;
  }
  .intro {
    font-size: 45px;
    line-height: 60px;
    text-align: justify;
    font-weight: 400;
  }
  .intro p { text-indent: 36px; margin-bottom: 60px; }
  .intro p:last-child { margin-bottom: 0; }
  .call-to-action {
    margin-top: 80px;
    text-align: center;
    font-weight: 700;
    font-size: 56px;
    line-height: 70px;
  }
  .contact {
    position: absolute;
    top: 2205px;
    left: 0;
    width: 1205px;
    text-align: center;
    font-style: normal;
  }
  .contact__name { font-weight: 600; font-size: 64px; line-height: 80px; }
  .contact__phone { font-size: 40px; margin-top: 36px; letter-spacing: 1px; }
  .contact__links { font-size: 36px; margin-top: 18px; line-height: 50px; }
</style>
</head>
<body>
<main class="flyer">
  <svg class="roof-art" width="1200" height="2506" viewBox="0 0 1200 2506" aria-hidden="true">
    <polygon class="eave" points="0,950 337,615 412,690 0,1102"/>
    <polygon class="eave" points="802,690 876,615 1205,944 1205,1093"/>
    <polygon class="house" points="603,532 1205,1132 1205,2506 0,2506 0,1135"/>
  </svg>

  <header class="brand-name">
    <div class="brand-name__mark"></div>
    <div class="brand-name__text">Kestrel<br>Electrics</div>
  </header>

  <h1 class="headline">Do you need<br>a local and reliable<br>electrician?</h1>

  <section class="body-copy">
    <div class="intro">
      <p>Specialising in residential and commercial electrical services, we are dedicated to providing customer service that is second to none.</p>
      <p>Whether you need a small wiring fix or a full installation, we can get the job done right.</p>
      <p>Based in Harbourvale, we are your local electricians, with our main aim to keep our work and communication to a very high standard.</p>
    </div>
    <p class="call-to-action">Contact us today!</p>
  </section>

  <address class="contact">
    <div class="contact__name">Dean Harwood</div>
    <div class="contact__phone">027 5832 094</div>
    <div class="contact__links">dean@kestrelelectrics-example.co.nz<br>www.kestrelelectrics-example.co.nz</div>
  </address>
</main>
</body>
</html>
```